Legal and business training card design

We need a business card design for POBAK - Pastoral Owners Bureau and Knowhow Agency a new company set up in county Victoria . Our aim is to assist regional business with their every day employment law legal issues and questions - this would include compliance within the workplace, employment conts, EBAs, dismissals, and general OHS. As well as POBAK will engage in training in particular Human Resources, management v leadership, time management , as well as constructing training around individual business/s needs. So we are multi purpose.
Our product is our service. It's designed specifically for regional base business hence we understand the requirements and needs of regional business v city business. At the same time the card must be simple, yet hard hitting, getting the message across in a couple of seconds.
I would like to see red and yellows, with perhaps a symbol/logo that represents the regional areas incorporated into the POBAK name ie curvy R in which the R's " right leg "expands under the entire acronym. Or you may have some better ideas. I also like the symbol of the square/s to match our slogan "shaping workplace answers beyond the fence line".
Thanks
Industry/Entity Type
Training
Contact Information for Business Card
POBAK
Pastoral Owners Bureau & Knowhow Agency
"shaping workplace answers beyond the fence line"
Fiona Brack B.A LL.B
Director and Principal
T: 1800 927 418 E: fiona@pobak.com.au
W: www.pobak.com.au

```html
<!DOCTYPE html>
<html lang="en">
<head>
<meta charset="utf-8">
<title>POBAK Stationery</title>
<link rel="stylesheet" href="https://fonts.googleapis.com/css2?family=Open+Sans:wght@400;600;700&display=swap">
<style>
  :root {
    --backdrop: #e4e4e4;
    --paper: #ffffff;
    --yellow: #ecc631;
    --red: #ee5a5a;
    --ink: #222222;
    --rule: #333333;
    --shadow: 0 6px 18px rgba(0,0,0,0.12);
  }
  * { box-sizing: border-box; margin: 0; padding: 0; }
  html, body {
    width: 1200px; height: 794px; overflow: hidden;
    background: var(--backdrop);
    font-family: "Open Sans", Arial, sans-serif;
    color: var(--ink);
  }
  .stationery { position: relative; width: 1200px; height: 794px; }

  .envelope {
    position: absolute; left: 320px; top: 60px;
    width: 560px; height: 310px;
    background: var(--paper); box-shadow: var(--shadow);
    display: flex; align-items: center; justify-content: center;
  }
  .brand { display: flex; align-items: center; gap: 8px; }
  .brand-square { width: 34px; height: 34px; background: var(--yellow); }
  .brand-name { font-weight: 600; font-size: 22px; color: var(--yellow); letter-spacing: 0.5px; white-space: nowrap; }

  .card {
    position: absolute; top: 430px;
    width: 340px; height: 200px;
    background: var(--paper); box-shadow: var(--shadow);
    overflow: hidden;
  }
  .card-front { left: 230px; }
  .card-back { left: 630px; }

  .card-front .front-content {
    position: absolute; left: 60px; top: 76px;
    display: flex; align-items: center; gap: 12px;
  }
  .card-front .brand-square { width: 26px; height: 26px; }
  .card-front .brand-name { font-size: 17px; }
  .divider { width: 1px; height: 44px; background: var(--rule); }
  .slogan { font-size: 10px; line-height: 1.3; white-space: nowrap; }

  .back-panel {
    position: absolute; left: 0; top: 92px;
    width: 118px; height: 78px;
    background: var(--yellow);
    display: flex; align-items: center; justify-content: center;
  }
  .back-panel .brand-name { color: var(--paper); font-size: 16px; }
  .back-divider { position: absolute; left: 132px; top: 70px; width: 1px; height: 90px; background: var(--rule); }
  .contact { position: absolute; left: 146px; top: 62px; white-space: nowrap; }
  .contact-name { font-size: 16px; font-weight: 400; line-height: 1.2; }
  .contact-role { font-size: 10px; font-weight: 700; margin-bottom: 6px; }
  .contact-line { font-size: 10px; line-height: 1.35; }
  .accent-bar { position: absolute; right: 0; top: 38px; width: 44px; height: 66px; background: var(--red); }
</style>
</head>
<body>
<main class="stationery">
  <section class="envelope">
    <div class="brand">
      <span class="brand-square"></span>
      <span class="brand-name">POBAK</span>
    </div>
  </section>

  <section class="card card-front">
    <div class="front-content">
      <div class="brand">
        <span class="brand-square"></span>
        <span class="brand-name">POBAK</span>
      </div>
      <span class="divider"></span>
      <p class="slogan">shaping workplace answers<br>beyond the fence line</p>
    </div>
  </section>

  <section class="card card-back">
    <div class="back-panel">
      <span class="brand-name">POBAK</span>
    </div>
    <span class="back-divider"></span>
    <div class="contact">
      <p class="contact-name">Fiona Brack B.A</p>
      <p class="contact-role">Director and Principal</p>
      <p class="contact-line">1800 927 418</p>
      <p class="contact-line">fiona@pobak.com.au</p>
      <p class="contact-line">www.pobak.com.au</p>
    </div>
    <span class="accent-bar"></span>
  </section>
</main>
</body>
</html>
```